Heal the world with your creativity.

We're looking for advertising materials (social media, email, etc) for a new mental health platform called PIVOT (www.viewpivot.tv). PIVOT’s mission is to empower our members to heal and thrive by making expert advice and real-life experiences accessible to all.

Note

Facebook Cover Images: 820 x 312 pixels
LinkedIn Cover Images: 1128 x 191 pixels
3 x Social Media Post Image Templates: 1080 x 1080 pixles
3 x Enewsletter Header Image Templates: 1080 x 360 pixels
Sales One sheet: US Letter (8.5 x 11 inches)
Overview Powerpoint template: 13.33 x 7.5 inches

Fonts to Use:
Galanogrotesque
Montserrat regular

Target Market(s)

18 - 35 year olds

Industry/Entity Type

Mental Health

Requirements
Must have
• Facebook Cover Images: 820 x 312 pixels
3 x Enewsletter Header Images: 1080 x 360 pixels

Fonts to Use:
Galanogrotesque
Montserrat regular
Nice to have
• Creative copywriting for social media posts

```html
<!DOCTYPE html>
<html lang="en">
<head>
<meta charset="utf-8">
<title>PIVOT — Your Mental Health Made Simple</title>
<link rel="stylesheet" href="https://fonts.googleapis.com/css2?family=Outfit:wght@600;700;800&display=swap">
<style>
  :root {
    --navy: #114a70;
    --ring: #2a6a96;
    --sky: #2f86c2;
    --orange: #f47f35;
    --white: #ffffff;
    --photo-warm: #d9a45c;
    --photo-mid: #b58a5a;
    --photo-deep: #5e6b4a;
  }
  * { margin: 0; padding: 0; box-sizing: border-box; }
  html, body {
    width: 1200px;
    height: 527px;
    overflow: hidden;
    background: var(--navy);
  }
  .cover {
    position: relative;
    width: 1200px;
    height: 527px;
    background: var(--navy);
    overflow: hidden;
    font-family: "Outfit", "Helvetica Neue", Arial, sans-serif;
  }
  .artwork {
    position: absolute;
    inset: 0;
    width: 1200px;
    height: 527px;
  }
  .brand {
    position: absolute;
    left: 51px;
    top: 51px;
    width: 190px;
    height: 190px;
    border-radius: 50%;
    background: var(--white);
    display: flex;
    align-items: center;
    justify-content: center;
  }
  .brand-name {
    color: var(--orange);
    font-weight: 800;
    font-size: 46px;
    letter-spacing: 1px;
  }
  .headline {
    position: absolute;
    left: 717px;
    top: 172px;
    color: var(--white);
  }
  .headline-kicker {
    display: block;
    font-weight: 700;
    font-size: 32px;
    line-height: 1;
    letter-spacing: 0.5px;
    margin-bottom: 22px;
  }
  .headline-main {
    display: block;
    font-weight: 700;
    font-size: 78px;
    line-height: 0.98;
    letter-spacing: 1px;
  }
</style>
</head>
<body>
  <main class="cover">
    <svg class="artwork" viewBox="0 0 1200 527" xmlns="http://www.w3.org/2000/svg">
      <defs>
        <clipPath id="portrait-clip">
          <circle cx="383" cy="310" r="241"/>
        </clipPath>
        <linearGradient id="portrait-tones" x1="0" y1="0" x2="1" y2="1">
          <stop offset="0" stop-color="var(--photo-deep)"/>
          <stop offset="0.45" stop-color="var(--photo-warm)"/>
          <stop offset="1" stop-color="var(--photo-mid)"/>
        </linearGradient>
      </defs>

      <circle class="halo-ring" cx="392" cy="344" r="293" fill="var(--ring)" opacity="0.8"/>
      <circle cx="392" cy="344" r="248" fill="var(--navy)"/>

      <g class="portrait" role="img" aria-label="Photo of a young woman in a beige puffer jacket outdoors in warm autumn light">
        <rect x="130" y="60" width="520" height="520" fill="url(#portrait-tones)" clip-path="url(#portrait-clip)"/>
      </g>

      <circle class="accent-orange-dot" cx="612" cy="278" r="25" fill="var(--orange)"/>
      <circle class="accent-blue-bubble" cx="644" cy="483" r="80" fill="var(--sky)" opacity="0.75"/>
      <circle class="accent-white-dot" cx="699" cy="468" r="10" fill="var(--white)"/>

      <circle class="corner-orange" cx="1051" cy="7" r="120" fill="var(--orange)"/>
      <circle class="corner-blue" cx="1127" cy="85" r="44" fill="var(--sky)" opacity="0.7"/>
    </svg>

    <div class="brand">
      <span class="brand-name">PIVOT</span>
    </div>

    <h1 class="headline">
      <span class="headline-kicker">YOUR MENTAL HEALTH</span>
      <span class="headline-main">MADE<br>SIMPLE.</span>
    </h1>
  </main>
</body>
</html>
```